Bright Meadow Website Design

About The Client:
Bright Meadow is a sugar-free foods chain store providing services to Diabetics. They focus on the China domestic market. They describe themselves as being the 3rd space for Diabetics, the space between hospital and the home that help improve the quality of life for people wit Diabetes (see attached infographics).

They regularly hold education and advice events throughout the China. Bright Meadow distribute a wide product range of food that is suitable for diabetic people. Bright Meadow operate as a Franchise, providing business development services and Industry knowledge. They are actively seeking business partnerships at present.

The Brief:
Design a Home page and secondary information page(PSD only no code) that communicates our company services and company philosophy(3rd Space).
The final design should communicate 'Health, Social Responsibility and Professionalism'.
Colour scheme should orientate around Blue and White, see attached logo.

Websites we like:

http://lantern.fenvoro.com/home/

https://www.quorvex.com/

http://wide.zt.com/
Updates

Hello all, the client has advised us that he want to display the professional advice service available for diabetic people more so than a food distributor. The client is also hoping to use his website as a marketing platform to attract affiliates and build partnerships as part of Bright Meadow's business expansion strategy.

So can you make the page more corporate, reliable and professional. Use images of experts/doctors interacting with patients and also training/knowledge transfer images.

Thanks

Hello all, could you include stock images of both Chinese and Caucasians

Yeaahhh, Infographics and photos have been uploaded. Feel free to use them in your designs and also as references.

Target Market(s)

The target market is Chinese B2B in the Diabetics industry and Entrepreneurs looking to cooperate with Bright Meadow.

Industry/Entity Type

Education

Requirements
Must have
• menu navigation with 7-8 sections,
a full screen background image,
Social Media icons,
Logo in top left,
Site search.
Nice to have
• The website must be clear and easy to use, less complicated.

See attached files of some Bright Meadow infographics. Feel free to include elements of these into the design.
Should not have
• Should not use stock images of people from any other country, the client wants stock images of Chinese people only. Avoid photos showing obesity.

```html
<!DOCTYPE html>
<html lang="en">
<head>
<meta charset="utf-8">
<title>Bright Meadow – Home</title>
<link href="https://fonts.googleapis.com/css2?family=Roboto+Condensed:wght@400;700&display=swap" rel="stylesheet">
<style>
:root{
  --blue:#1479c4;
  --blue-light:#1fa3e6;
  --blue-dark:#0d64a8;
  --red:#e02b35;
  --text:#555;
  --nav:#444;
  --page:#f3f2f2;
  --white:#fff;
  --border:#d5d5d5;
}
*{margin:0;padding:0;box-sizing:border-box}
html,body{width:1188px;height:1200px;overflow:hidden}
body{position:relative;background:var(--page);font-family:"Roboto Condensed",Arial,sans-serif;color:var(--text)}

.site-header{position:absolute;left:0;top:0;width:1188px;height:104px;background:var(--white);box-shadow:0 2px 4px rgba(0,0,0,.25);z-index:2}
.brand{position:absolute;left:179px;top:34px;display:flex;align-items:center;gap:8px;font-size:22px;font-weight:700;color:var(--blue-light)}
.brand-dot{width:14px;height:14px;background:var(--red)}
.social-links{position:absolute;right:345px;top:25px;display:flex;gap:10px;font-size:13px;font-weight:700;color:var(--blue)}
.social-links a{color:inherit;text-decoration:none;white-space:nowrap}
.search{position:absolute;left:855px;top:16px;width:180px;height:32px;border:1px solid var(--border);background:var(--white);font-size:14px;color:#666;padding:7px 8px}
.search svg{position:absolute;right:8px;top:7px}
.main-nav{position:absolute;top:68px;left:0;font-size:15.5px;color:var(--nav)}
.main-nav a{position:absolute;white-space:nowrap;text-decoration:none;color:inherit}
.main-nav a.active{color:var(--blue-light)}
.nav-underline{position:absolute;left:441px;top:100px;width:62px;height:4px;background:var(--blue-light)}

.hero{position:absolute;left:0;top:104px;width:1188px;height:444px;background:linear-gradient(100deg,#e9ecef 0%,#f7f8f9 30%,#dfe7ee 55%,#c9b8a8 75%,#e8e8e8 100%)}
.slider-dots{position:absolute;left:532px;top:530px;width:108px;height:34px;border-radius:0 0 18px 18px;background:var(--white);box-shadow:0 3px 5px rgba(0,0,0,.2);display:flex;justify-content:center;align-items:center;gap:10px}
.slider-dots span{width:13px;height:13px;border-radius:50%;border:1px solid #bbb;background:#eee}
.slider-dots span.on{background:#ccc}

.card{position:absolute;top:591px;width:288px;height:252px;background:#efefef;border:1px solid var(--border)}
.card h2{position:absolute;top:14px;width:100%;text-align:center;font-size:16px;font-weight:700;color:var(--blue-dark)}
.card-photo{position:absolute;left:16px;top:41px;width:253px;height:102px;border:1px solid #ccc;background:var(--white);padding:4px}
.card-photo div{width:100%;height:100%}
.card p{position:absolute;left:12px;right:12px;top:149px;text-align:center;font-size:12.5px;line-height:15px}
.btn-small{position:absolute;left:82px;top:203px;width:114px;height:30px;border-radius:2px;background:linear-gradient(#27aef0,#0e82cb);color:var(--white);font-size:12.5px;font-weight:700;text-align:center;line-height:30px}

.section-title{position:absolute;top:866px;font-size:16px;font-weight:400;color:var(--text)}
.section-title b{color:var(--blue-dark)}
.dashed{position:absolute;top:894px;height:0;border-top:1px dashed #aaa}
.welcome-text{position:absolute;left:147px;top:905px;width:588px;font-size:12.3px;line-height:14.6px}
.btn-big{position:absolute;top:988px;width:190px;height:46px;border-radius:3px;color:var(--white);font-size:15px;font-weight:700;text-align:center;line-height:46px;text-transform:uppercase}
.btn-blue{background:linear-gradient(#2ab0ef 0%,#1c9ee0 48%,#0f87cf 52%,#0d7fc4 100%);border:1px solid #0d70b0}
.btn-red{background:linear-gradient(#f0505a 0%,#e63a45 48%,#d8222d 52%,#cc1c26 100%);border:1px solid #b3151e}

.field{position:absolute;left:746px;width:291px;background:var(--white);border:1px solid var(--border);font-size:13px;color:#555;padding:8px 6px}
.btn-submit{position:absolute;left:923px;top:1043px;width:114px;height:30px;border-radius:2px;background:linear-gradient(#27aef0,#0e82cb);color:var(--white);font-size:13px;font-weight:700;text-align:center;line-height:30px}

.site-footer{position:absolute;left:0;top:1104px;width:1188px;height:96px;background:var(--white);border-top:1px solid #ddd;text-align:center;font-size:12px;color:#555;padding-top:30px;line-height:17px}
</style>
</head>
<body>

<header class="site-header">
  <div class="brand"><span class="brand-dot"></span>Bright Meadow</div>
  <div class="social-links">
    <a href="#" aria-label="Follow us on Chirply">Chirply</a>
    <a href="#" aria-label="Follow us on Friendlink">Friendlink</a>
  </div>
  <div class="search">Search
    <svg width="18" height="18" viewBox="0 0 18 18"><circle cx="7" cy="7" r="5.5" fill="none" stroke="#4a7fb5" stroke-width="1.6"/><line x1="11" y1="11" x2="16.5" y2="16.5" stroke="#4a7fb5" stroke-width="2"/></svg>
  </div>
  <nav class="main-nav">
    <a class="active" style="left:455px">Home</a>
    <a style="left:519px">About Us</a>
    <a style="left:603px">Services</a>
    <a style="left:681px">Food Store</a>
    <a style="left:775px">Our Philosophy</a>
    <a style="left:894px">Events</a>
    <a style="left:963px">Contact Us</a>
  </nav>
  <div class="nav-underline"></div>
</header>

<div class="hero" role="img" aria-label="Store interior with advisor talking to customers in front of lit product shelves"></div>
<div class="slider-dots"><span class="on"></span><span></span><span></span><span></span></div>

<section class="card" style="left:146px">
  <h2>Our Philosophy</h2>
  <div class="card-photo"><div role="img" aria-label="Woman stretching happily in a bright room" style="background:linear-gradient(90deg,#d6d6d6,#f2f2f2,#cfcfcf)"></div></div>
  <p>Lorem ipsum dolor sit amet, consectetur adipisicing elit, sed do eiusmod tempor incididunt ut labore et dolore magna aliqua.</p>
  <div class="btn-small">Know More</div>
</section>
<section class="card" style="left:447px">
  <h2>Our Services</h2>
  <div class="card-photo"><div role="img" aria-label="Smiling staff member at a store counter" style="background:linear-gradient(90deg,#dfe6ec,#f1ede8,#d8dfe5)"></div></div>
  <p>Lorem ipsum dolor sit amet, consectetur adipisicing elit, sed do eiusmod tempor incididunt ut labore et dolore magna aliqua.</p>
  <div class="btn-small">Know More</div>
</section>
<section class="card" style="left:748px">
  <h2>Our Events</h2>
  <div class="card-photo"><div role="img" aria-label="Customers gathered in a store with colourful product shelves" style="background:linear-gradient(90deg,#c98f5a,#7fb0d8,#d6a066)"></div></div>
  <p>Lorem ipsum dolor sit amet, consectetur adipisicing elit, sed do eiusmod tempor incididunt ut labore et dolore magna aliqua.</p>
  <div class="btn-small">Know More</div>
</section>

<h3 class="section-title" style="left:147px"><b>Welcome</b> to our site</h3>
<div class="dashed" style="left:147px;width:588px"></div>
<p class="welcome-text">Lorem ipsum dolor sit amet, consectetur adipisicing elit, sed do eiusmod tempor incididunt ut labore et dolore magna aliqua. Lorem ipsum dolor sit amet, consectetur adipisicing elit, sed do eiusmod tempor incididunt ut labore et dolore magna aliqua. Lorem ipsum dolor sit amet, consectetur adipisicing elit, sed do eiusmod tempor incididunt ut labore et dolore magna aliqua.</p>
<div class="btn-big btn-blue" style="left:147px">Our Training</div>
<div class="btn-big btn-red" style="left:345px">Pertnership</div>
<div class="btn-big btn-blue" style="left:542px">For Diabetics</div>

<h3 class="section-title" style="left:747px"><b>Query Us</b> to help you</h3>
<div class="dashed" style="left:747px;width:290px"></div>
<div class="field" style="top:906px;height:31px">Email</div>
<div class="field" style="top:944px;height:90px">Query</div>
<div class="btn-submit">Submit</div>

<footer class="site-footer">
  Copyright@2013, All rights are reserved.<br>Terms &amp; Privacy Policy
</footer>

</body>
</html>
```